Business Card Design Project

I help solve problems that people have with real estate, so I buy homes for cash that they no longer want, can't afford, inherited, etc. and fix and sell them or rent them or take over mortgage payments. See website: www.quickdeedhomestead.com

Industry/Entity Type

Real Estate

Contact Information for Business Card

Not exactly sure. Looking for a design that either is similar to the website www.quickdeedhomestead.com or that reflects what I do as described below. If it can look a little luxurious to show I can buy the houses for cash and I fix them and sell them, it's a bonus. I seem to like some of the higher end things like foil or black or something that makes it stand out.

Font styles to use
Serif

Requirements
Nice to have
• I seem to like black or clear. I like things to stand out and be different.

```html
<!DOCTYPE html>
<html lang="en">
<head>
<meta charset="utf-8">
<title>Quickdeed Homestead – Business Card</title>
<link href="https://fonts.googleapis.com/css2?family=Roboto:wght@400;500&display=swap" rel="stylesheet">
<style>
  :root{
    --page-bg:#d9d6d2;
    --green-light:#6fb83a;
    --green-mid:#4f9a2a;
    --green-dark:#3c7f1f;
    --frost:#e4e3df;
    --frost-shadow:#c9c8c4;
    --edge:#151a12;
    --band:#1d1a1c;
    --text-light:#f2f2ee;
    --text-soft:#e6e2e2;
    --brand-green:#3f8d22;
  }
  html,body{margin:0;padding:0;width:1200px;height:1054px;overflow:hidden;background:var(--page-bg);}
  .card{
    position:absolute;left:100px;top:225px;width:1000px;height:605px;
    font-family:"Roboto",Arial,sans-serif;
    box-shadow:0 10px 30px rgba(0,0,0,.18);
    overflow:hidden;
  }
  .card-art{position:absolute;inset:0;}
  .holder-name{position:absolute;left:57px;top:96px;margin:0;font-size:36px;font-weight:500;color:var(--text-light);}
  .holder-title{position:absolute;left:58px;top:150px;margin:0;font-size:24px;font-weight:400;color:var(--text-soft);}
  .contact-list{position:absolute;left:57px;top:322px;margin:0;padding:0;list-style:none;}
  .contact-list li{display:flex;align-items:center;height:34px;font-size:23px;color:var(--text-light);}
  .contact-list svg{width:22px;height:22px;margin-right:16px;fill:var(--text-soft);}
  .tagline{position:absolute;left:66px;top:500px;margin:0;font-size:23px;color:var(--text-soft);}
  .brand-name{
    position:absolute;left:670px;top:284px;width:320px;margin:0;
    text-align:center;font-size:27px;font-weight:500;color:var(--brand-green);
    white-space:nowrap;
  }
</style>
</head>
<body>
<div class="card">
  <svg class="card-art" viewBox="0 0 1000 605" width="1000" height="605">
    <defs>
      <linearGradient id="greenPanel" x1="0" y1="0" x2="1" y2="1">
        <stop offset="0" stop-color="var(--green-light)"/>
        <stop offset=".55" stop-color="var(--green-mid)"/>
        <stop offset="1" stop-color="var(--green-dark)"/>
      </linearGradient>
      <linearGradient id="frostPanel" x1="0" y1="0" x2="1" y2="0">
        <stop offset="0" stop-color="var(--frost-shadow)"/>
        <stop offset=".4" stop-color="var(--frost)"/>
        <stop offset="1" stop-color="#ecebe7"/>
      </linearGradient>
    </defs>
    <rect class="frost-panel" width="1000" height="605" fill="url(#frostPanel)"/>
    <path class="curve-edge" d="M0 0 H686 Q600 302 686 605 H0 Z" fill="var(--edge)"/>
    <path class="green-panel" d="M0 0 H675 Q590 302 675 605 H0 Z" fill="url(#greenPanel)"/>
    <path class="tagline-band" d="M0 490 H618 Q623 518 632 544 H0 Z" fill="var(--band)"/>
  </svg>

  <h1 class="holder-name">Jonah Reed Carter</h1>
  <p class="holder-title">Managing Director</p>

  <ul class="contact-list">
    <li><svg viewBox="0 0 24 24"><path d="M3 9c0-3 4-5 9-5s9 2 9 5v2h-5V9H8v2H3z M6 12h12l2 8H4z"/></svg>224-555-SOLD</li>
    <li><svg viewBox="0 0 24 24"><path d="M2 5h20v14H2z M3.5 6.5 12 13l8.5-6.5" fill="none" stroke="var(--text-soft)" stroke-width="2"/></svg>jcarter@quickdeedhomestead.com</li>
    <li><svg viewBox="0 0 24 24"><circle cx="12" cy="12" r="9" fill="none" stroke="var(--text-soft)" stroke-width="2"/><path d="M3 12h18M12 3c-4 5-4 13 0 18M12 3c4 5 4 13 0 18" fill="none" stroke="var(--text-soft)" stroke-width="1.6"/></svg>www.quickdeedhomestead.com</li>
  </ul>

  <p class="tagline">Selling and Buying Houses in Illinois</p>

  <p class="brand-name">Quickdeed Homestead</p>
</div>
</body>
</html>
```